Flyer-Design für Schamanismus-Pferde-Musik
Vielen Dank, es war eine tolle Zusammenarbeit, mit vielen kreativen Vorschlägen Seitens der Designerin und einer sehr schnellen, guten Umsetzung meiner Änderungswünsche!
Zielgruppe
Schamanismus-Pferde-Musik
schamanische Heilarbeit im grünen Haus ;-)
Einzel- und Gruppencoaching mit PFERD zur Persönlichkeitsentwicklung
Aufgabenstellung
ich persönlich finde quadratische Flyer sehr schön...

```html
<!DOCTYPE html>
<html lang="de">
<head>
<meta charset="utf-8">
<title>Flyer Schamanismus · Pferde · Musik</title>
<link rel="stylesheet" href="https://fonts.googleapis.com/css2?family=Fira+Sans+Extra+Condensed:wght@500;600;700&family=Quicksand:wght@400;500;600;700&display=swap">
<style>
:root{
  --red:#c1272d;
  --ink:#3a3a3a;
  --line:#9a9a9a;
  --paper:#ffffff;
  --bg:#e4e3e3;
  --cond:"Fira Sans Extra Condensed",sans-serif;
  --body:"Quicksand",sans-serif;
}
*{box-sizing:border-box;margin:0;padding:0}
html,body{width:1200px;height:2880px;overflow:hidden}
body{position:relative;background:var(--bg);font-family:var(--body);color:var(--ink)}
.spread{position:absolute;left:88px;width:1026px;height:512px;display:flex;gap:4px}
.spread--one{top:885px}
.spread--two{top:1482px}
.page{position:relative;width:511px;height:512px;background:var(--paper);overflow:hidden}
.abs{position:absolute}
.frame{position:absolute;inset:0;width:100%;height:100%}
.photo{position:absolute}
.red-box{position:absolute;background:var(--red);color:#fff;text-align:center}
.cond{font-family:var(--cond);font-weight:600}
.title{position:absolute;font-family:var(--cond);font-weight:700;color:var(--red);text-align:center}
.quote{position:absolute;font-size:8.6px;line-height:1.32;text-align:center;color:var(--ink)}
.small{font-size:8px;line-height:1.35}
.offer-list{list-style:none}
.offer-list li{display:flex;align-items:center;gap:8px;font-size:10px;height:21px}
.offer-list svg{flex:none}
.offer-note{font-size:7px}
.module-head{font-family:var(--cond);font-weight:600;color:var(--red);font-size:11px;padding-bottom:3px;border-bottom:1px solid var(--line);margin-bottom:4px}
.module p{font-size:7.6px;line-height:1.3;display:flex;gap:6px}
.module p b{color:var(--red);font-weight:500}
.module{margin-bottom:14px}
</style>
</head>
<body>

<section class="spread spread--one">
  <article class="page page--feedback">
    <svg class="frame" viewBox="0 0 511 512" aria-hidden="true">
      <path d="M32 28 V478 M44 18 H458 M36 495 H470" stroke="var(--line)" stroke-width="1" fill="none"/>
    </svg>
    <div class="photo" role="img" aria-label="Schwarzweiß-Porträt einer Geigerin, die Geige am Kinn" style="left:45px;top:31px;width:179px;height:274px;background:linear-gradient(160deg,#2a2522,#7a6a60 45%,#d9cfc6 70%,#3a302c)"></div>
    <div class="red-box" style="left:45px;top:316px;width:179px;height:196px;padding-top:14px">
      <div class="cond" style="font-size:16px">Die mit der Geige tanzt</div>
      <div class="small" style="margin-top:12px;opacity:.9">bekannt durch die von ihr<br>mitgegründete Band <b>Mondharfe</b></div>
      <div class="small" style="margin-top:12px;text-align:left;padding-left:28px;font-weight:600">Birtel Hovsmann<br>Lindenweg 7<br>94560 Talbrunn (Auwald)</div>
      <div class="small" style="margin-top:8px;text-align:left;padding-left:20px;font-weight:600">&#9990; 0170/5550123</div>
      <div class="cond" style="font-size:14px;margin-top:6px">Info &amp; Anmeldung</div>
      <div class="small" style="font-weight:600">&#9679; www.wald-ross-klang.de</div>
    </div>
    <div class="photo" role="img" aria-label="Frau streichelt ein weißes Pony im Wald" style="left:233px;top:316px;width:248px;height:196px;background:linear-gradient(135deg,#5a6a3a,#9aa070 40%,#e8e6e0 60%,#6b6a5a)"></div>
    <div class="title" style="left:250px;top:28px;width:200px;font-size:24px">Feedback</div>
    <p class="quote" style="left:248px;top:72px;width:210px">„Es war genau das was ich gebraucht habe! Hab danach einiges im Leben geändert, wozu mir sonst immer der Mut, die Kraft und Energie gefehlt hat! Ich habe einen neuen Job ab August, genau das, was ich gesucht habe! Ich wohne jetzt in einer neuen kleinen Wohnung! Fühle mich richtig gut! Manchmal braucht man einfach wirklich nur eine Auszeit, um Ruhe und Kraft zu tanken! Danke dafür und ganz besonders für die Flussreise!“</p>
    <p class="quote" style="left:248px;top:184px;width:210px">„Mir hat die Möglichkeit mich so unbefangen den Pferden zu nähern die schönsten Erfahrungen gebracht. Das dauert bis ich alles verstanden habe, aber es tat sehr gut und ich schöpfe Kraft daraus.“</p>
    <p class="quote" style="left:248px;top:248px;width:210px">„Bei Dir konnte ich loslassen und voranschreiten – saugut! Eine tolle Erfahrung.“</p>
  </article>

  <article class="page page--cover">
    <svg class="frame" viewBox="0 0 511 512" aria-hidden="true">
      <path d="M30 495 H470 M480 28 V478 M50 18 H458" stroke="var(--line)" stroke-width="1" fill="none"/>
    </svg>
    <div class="photo" role="img" aria-label="Grünes Haus am Waldrand hinter einer Wiese" style="left:47px;top:31px;width:414px;height:148px;background:linear-gradient(180deg,#3b4a2c,#5f6e40 60%,#b8a070 85%,#8a7a50)"></div>
    <div class="abs" style="left:140px;top:48px;color:#fff;font-family:var(--body);font-size:16px;font-weight:500;letter-spacing:2px">birtel hovsmann</div>
    <div class="photo" role="img" aria-label="Nahaufnahme eines weißen Pferdekopfes mit Hand" style="left:47px;top:188px;width:123px;height:285px;background:linear-gradient(160deg,#5a4a40,#d8d0c6 40%,#f1ece6 70%,#8a7a6a)"></div>
    <div class="red-box cond" style="left:182px;top:190px;width:166px;height:65px;padding-top:9px;font-size:13.5px;line-height:1.25">Schamanische Heilarbeit<br>&amp; pferdegestützte<br>Persönlichkeitsentwicklung</div>
    <div class="photo" role="img" aria-label="Frau mit Rahmentrommel und schwarzer Hund auf einem Weg" style="left:182px;top:266px;width:166px;height:184px;background:linear-gradient(150deg,#6a4a3a,#8a8a6a 45%,#5a5a4a 70%,#2a2a2a)"></div>
    <div class="photo" role="img" aria-label="Hand hält eine Feder vor einer Jeansjacke" style="left:359px;top:188px;width:102px;height:285px;background:linear-gradient(160deg,#a05a30,#5a6a8a 45%,#3a4a6a 75%,#c9a48a)"></div>
    <div class="red-box cond" style="left:182px;top:458px;width:279px;height:17px;font-size:12px;line-height:17px">www.wald-ross-klang.de</div>
  </article>
</section>

<section class="spread spread--two">
  <article class="page page--healing">
    <svg class="frame" viewBox="0 0 511 512" aria-hidden="true">
      <path d="M32 28 V478 M44 18 H480 M36 495 H470" stroke="var(--line)" stroke-width="1" fill="none"/>
    </svg>
    <div class="photo" role="img" aria-label="Frau sitzt meditierend im sonnigen Wald" style="left:45px;top:34px;width:210px;height:218px;background:linear-gradient(170deg,#c9d2a8,#6a7a3a 40%,#4a5a2a 70%,#8a6a4a)"></div>
    <div class="red-box cond" style="left:255px;top:34px;width:226px;height:48px;padding-top:8px;font-size:12px;line-height:1.3">Schamanismus ist keine Religion,<br>es ist eine Lebenseinstellung!</div>
    <div class="title" style="left:255px;top:92px;width:226px;font-size:20px">Schamanische Heilarbeit:</div>
    <p class="quote" style="left:262px;top:128px;width:212px;font-size:8.2px">Eins sein mit der Natur und allen Wesen um uns. Jeder Baum, jeder Stein, jedes Tier hat eine Seele. Auch unsere Ahnen spielen eine große Rolle.<br><br>In der schamanischen Ansicht hängen Körper und Seele zusammen. Somit liegt die Lösung für unsere Beschwerden in unserem Inneren. Der Schamane verbindet sich mit der geistigen Welt und lässt seine heilenden Kräfte von dieser leiten.</p>
    <div class="photo" role="img" aria-label="Menschen sitzen nachts um ein loderndes Feuer" style="left:255px;top:252px;width:209px;height:224px;background:radial-gradient(ellipse at 50% 65%,#f08a30,#b8401a 35%,#2a1a1a 75%)"></div>
    <div class="abs" style="left:255px;top:262px;width:209px;text-align:center;color:#fff;font-size:11px;font-weight:600">www.wald-ross-klang.de</div>
    <div class="title" style="left:80px;top:262px;width:140px;font-size:18px">Angebote:</div>
    <ul class="offer-list abs" style="left:45px;top:292px;width:210px">
      <li><svg width="12" height="12" viewBox="0 0 12 12"><circle cx="6" cy="6" r="5" fill="none" stroke="var(--red)" stroke-width="1.3"/><path d="M3.5 6 l2 2 l4 -5" stroke="var(--red)" stroke-width="1.6" fill="none"/></svg>Chakrenreinigung</li>
      <li><svg width="12" height="12" viewBox="0 0 12 12"><circle cx="6" cy="6" r="5" fill="none" stroke="var(--red)" stroke-width="1.3"/><path d="M3.5 6 l2 2 l4 -5" stroke="var(--red)" stroke-width="1.6" fill="none"/></svg>Rückholung verlorener Seelenanteile</li>
      <li><svg width="12" height="12" viewBox="0 0 12 12"><circle cx="6" cy="6" r="5" fill="none" stroke="var(--red)" stroke-width="1.3"/><path d="M3.5 6 l2 2 l4 -5" stroke="var(--red)" stroke-width="1.6" fill="none"/></svg><span>Reinigung mit Heilsteinen <span class="offer-note">(Ila Moor)</span></span></li>
      <li><svg width="12" height="12" viewBox="0 0 12 12"><circle cx="6" cy="6" r="5" fill="none" stroke="var(--red)" stroke-width="1.3"/><path d="M3.5 6 l2 2 l4 -5" stroke="var(--red)" stroke-width="1.6" fill="none"/></svg>Heilarbeit mit Tieren</li>
      <li><svg width="12" height="12" viewBox="0 0 12 12"><circle cx="6" cy="6" r="5" fill="none" stroke="var(--red)" stroke-width="1.3"/><path d="M3.5 6 l2 2 l4 -5" stroke="var(--red)" stroke-width="1.6" fill="none"/></svg>Hausreinigung (bei Ihnen Zuhause)</li>
      <li><svg width="12" height="12" viewBox="0 0 12 12"><circle cx="6" cy="6" r="5" fill="none" stroke="var(--red)" stroke-width="1.3"/><path d="M3.5 6 l2 2 l4 -5" stroke="var(--red)" stroke-width="1.6" fill="none"/></svg>Schamanische Reisen</li>
      <li><svg width="12" height="12" viewBox="0 0 12 12"><circle cx="6" cy="6" r="5" fill="none" stroke="var(--red)" stroke-width="1.3"/><path d="M3.5 6 l2 2 l4 -5" stroke="var(--red)" stroke-width="1.6" fill="none"/></svg>Arbeit mit Krafttieren</li>
      <li><svg width="12" height="12" viewBox="0 0 12 12"><circle cx="6" cy="6" r="5" fill="none" stroke="var(--red)" stroke-width="1.3"/><path d="M3.5 6 l2 2 l4 -5" stroke="var(--red)" stroke-width="1.6" fill="none"/></svg>Persönlichkeitsentwicklung</li>
    </ul>
    <div class="abs" style="left:65px;top:466px;font-size:7.5px">u.v.m. – je nach dem, was individuell ruft.</div>
  </article>

  <article class="page page--horses">
    <svg class="frame" viewBox="0 0 511 512" aria-hidden="true">
      <path d="M250 18 H460 M480 28 V478 M250 495 H470" stroke="var(--line)" stroke-width="1" fill="none"/>
    </svg>
    <div class="photo" role="img" aria-label="Geigerin sitzt spielend auf einem schwarzen Pferd im Wald" style="left:0;top:22px;width:237px;height:363px;background:linear-gradient(170deg,#3a4a2a,#6a7a4a 35%,#2a2a24 65%,#1a1a18)"></div>
    <div class="red-box" style="left:0;top:385px;width:237px;height:107px;padding:10px 14px 0">
      <div style="font-size:7.8px;line-height:1.3">Heilsitzungen sind auch aus der <b>Ferne</b> möglich! Dazu machen wir einen Termin aus, an dem Sie sich an einem ungestörten Ort Ihrer Wahl für ca. eine Stunde Zeit nehmen müssen.</div>
      <div class="cond" style="font-size:11.5px;margin-top:8px">Monatliche Veranstaltungen</div>
      <div style="font-size:7.6px;line-height:1.3;margin-top:3px">Naturtage, Rauhnachtszeremonie, Feuerzeremonie, Vollmondtrommeln, Frauenkreise…</div>
    </div>
    <div class="title" style="left:248px;top:32px;width:220px;font-size:19px;line-height:1.1">Pferdegestützte<br>Persönlichkeitsentwicklung</div>
    <div class="abs" style="left:248px;top:80px;width:220px;text-align:center;font-size:7.6px;line-height:1.3"><span style="color:var(--red)">KEINE Reiterfahrung oder Pferdekenntnis notwendig.</span><br>Wir machen alle Übungen vom Boden aus!</div>
    <p class="quote" style="left:256px;top:110px;width:204px;font-size:9.6px">Pferde sind die Spiegel unserer Seele. Wenn wir authentisch sind, wird ein Pferd mit uns freiwillig Kontakt aufnehmen.<br><br>Diese wunderbaren, kraftvollen Wesen helfen uns, innerste Wünsche aufzudecken, Trauer zu verarbeiten, Kraft zu tanken und wahrhaftige Kommunikation wieder zu erlernen – die nichts mit „viel reden“ zu tun hat…</p>
    <div class="abs" style="left:258px;top:262px;width:200px">
      <div class="module"><div class="module-head">Sprenge Deine Grenzen &amp; Lebe Deinen Traum!</div><p><span>&#9679;</span><span><b>Zielgruppe:</b> Privatpersonen, die etwas in ihrem Leben verändern wollen, aber noch nach dem Weg dahin suchen.</span></p></div>
      <div class="module"><div class="module-head">Baue Dein Team</div><p><span>&#9679;</span><span><b>Zielgruppe:</b> Gruppen jeglicher Art, ob Jugendgruppen, Bands, Gemeinschaften, Familien</span></p></div>
      <div class="module"><div class="module-head">Die Kunst des Führens</div><p><span>&#9679;</span><span><b>Zielgruppe:</b> Führungskräfte in Firmen, Lehrer, Mütter – alle, die eine Gruppe zu leiten haben.</span></p></div>
    </div>
  </article>
</section>
</body>
</html>
```